Harbor Wonder Hour - A magic website for a monthly modern magic show

Looking to build a website to promote my new monthly magic show

Sites like this. https://velvetloftshow.example/ https://brasslanterntricks.example/

Target Market(s)

18-65 year old men and women who enjoy live entertainment especially magic

Industry/Entity Type

Entertainment

Coding

Coded - Design and coding required

Number of Pages Required

3 page

Colors

Designer to choose colors to be used in the design.

Requirements
Must have
• Wanting a wordpress site.
• Contact form, media section for photos and videos to be posted.
• A “reviews/testimonials” section.

```html
<!DOCTYPE html>
<html lang="en">
<head>
<meta charset="utf-8">
<title>Harbor Wonder Hour</title>
<link href="https://fonts.googleapis.com/css2?family=Playfair+Display:wght@400;700;900&family=Josefin+Sans:wght@400;600&family=Spectral:wght@400&display=swap" rel="stylesheet">
<style>
:root{
  --bg:#0c0c0e;
  --panel:#222224;
  --panel-dark:#19191b;
  --accent:#ef7a45;
  --text:#f2f2f2;
  --muted:#a9a9a9;
  --line:#4a4a4a;
}
*{margin:0;padding:0;box-sizing:border-box}
html,body{width:1200px;height:5079px;overflow:hidden;background:var(--bg)}
body{position:relative;color:var(--text);font-family:"Josefin Sans",sans-serif;
  background:
   radial-gradient(ellipse 700px 500px at 600px 350px,#1f1b2a 0%,transparent 70%),
   radial-gradient(ellipse 600px 400px at 300px 2400px,#1c1c1e 0%,transparent 70%),
   radial-gradient(ellipse 600px 400px at 900px 3300px,#1a1a1c 0%,transparent 70%),
   var(--bg)}
.abs{position:absolute}
.serif{font-family:"Spectral",serif}
.display{font-family:"Playfair Display",serif}
.outline-title{position:absolute;left:0;width:1200px;text-align:center;font-family:"Playfair Display",serif;font-weight:900;font-size:46px;letter-spacing:2px;color:transparent;-webkit-text-stroke:1.2px #9a9a9a}

/* nav */
.brand{left:95px;top:29px;font-size:14px;font-weight:600;letter-spacing:1px;text-transform:uppercase}
.nav{top:30px;left:670px;display:flex;gap:34px;font-size:12px;font-weight:600;letter-spacing:1px}
.nav-btn{left:965px;top:20px;width:142px;height:35px;border:1px solid #cfcfcf;font-size:12px;font-weight:600;letter-spacing:1px;display:flex;align-items:center;justify-content:center}

/* hero */
.hero-photo{left:170px;top:60px;width:860px;height:560px;background:radial-gradient(ellipse at 50% 45%,#3a3a44 0%,#1b1a22 55%,transparent 80%)}
.hero-frame{left:467px;top:115px;width:268px;height:742px;border:7px solid var(--accent)}
.hero-title{left:0;width:1200px;text-align:center;font-family:"Playfair Display",serif;font-weight:900}
.hero-title.big{top:608px;font-size:92px;letter-spacing:3px}
.hero-title.small{top:702px;font-size:56px;letter-spacing:2px}

/* about */
.emblem{left:80px;top:930px;width:480px;height:490px;border-radius:50%;background:radial-gradient(circle,#1d1d20 0%,#121214 60%,transparent 72%)}
.emblem-name{left:190px;top:1105px;width:380px;font-family:"Playfair Display",serif;font-weight:700;font-size:44px;line-height:55px;color:#b9b9b9}
.about-label{left:628px;top:1060px;color:var(--accent);font-size:14px;letter-spacing:2px}
.about-lead{left:628px;top:1092px;width:360px;font-size:15px;line-height:22px;color:#dcdcdc}
.about-body{left:628px;top:1208px;width:355px;font-size:11.5px;line-height:18px;color:#bdbdbd}
.card-art{left:1010px;top:1030px;width:190px;height:360px;background:linear-gradient(160deg,#2a2a2d,#0f0f11)}

/* monthly show */
.side-card{top:1742px;width:132px;height:283px;background:var(--panel-dark)}
.side-card .img{position:absolute;top:0;width:82px;height:283px;background:linear-gradient(#2a2a2c,#151516)}
.side-date{position:absolute;top:22px;width:50px;text-align:center;color:#777;font-size:10px;line-height:14px}
.side-date b{display:block;font-size:24px;font-weight:400;font-family:"Spectral",serif;line-height:26px}
.side-text{position:absolute;top:80px;writing-mode:vertical-rl;font-family:"Spectral",serif;font-size:12px;color:#888;height:180px}
.show-photo{left:255px;top:1707px;width:345px;height:318px;background:linear-gradient(135deg,#2b2b30 0%,#141416 100%)}
.show-card{left:600px;top:1670px;width:347px;height:415px;background:var(--panel);padding:45px 45px}
.kicker{font-size:11px;color:#7d7d7d;letter-spacing:.5px;text-transform:uppercase}
.card-title{font-family:"Spectral",serif;font-size:19px;line-height:24px;margin-top:18px}
.card-copy{font-size:11px;line-height:18px;color:#bdbdbd;margin-top:18px}
.meta{display:flex;align-items:center;gap:12px;font-size:10.5px;color:#ddd;margin-top:14px}
.btn{display:inline-flex;align-items:center;justify-content:center;border:1px solid var(--accent);color:var(--accent);font-size:12px;letter-spacing:1px;height:31px;padding:0 22px}
.pager{left:0;width:1200px;display:flex;justify-content:center;align-items:center;gap:30px;font-family:"Spectral",serif;font-size:24px}
.pager small{font-size:13px;color:#aaa}

/* video */
.side-word{font-family:"Playfair Display",serif;font-weight:900;font-size:100px;color:transparent;-webkit-text-stroke:1.5px #3a3a3a;writing-mode:vertical-rl}
.video{left:185px;top:2253px;width:833px;height:430px;background:radial-gradient(ellipse at 50% 55%,#3a3a3e 0%,#18181a 70%)}
.video-title{left:220px;top:2283px;font-size:14px}
.play{left:555px;top:2426px}

/* review */
.stars{left:0;width:1200px;top:2838px;display:flex;justify-content:center;gap:8px}
.quote{left:140px;width:920px;top:2883px;text-align:center;font-family:"Spectral",serif;font-size:16.5px;line-height:22px;color:#cfcfcf}
.author{left:0;width:1200px;top:2970px;text-align:center;font-family:"Spectral",serif;font-size:17px;color:var(--accent)}

/* news */
.news-card{width:450px;height:415px;background:var(--panel);padding:45px 46px}
.news-card .card-copy{margin-bottom:44px}

/* contact */
.wand-art{left:900px;top:3790px;width:215px;height:130px;background:linear-gradient(200deg,#2b2b2e,transparent)}
.field{border:1px solid var(--line);font-size:11px;color:#8a8a8a;padding:18px 30px}
.submit{left:525px;top:4225px;width:150px;height:37px}

/* footer */
.socials{left:505px;top:4425px;display:flex;gap:10px}
.socials span{width:42px;height:42px;border-radius:50%;background:#f0f0f0}
.call{left:0;width:1200px;top:4468px;text-align:center;font-family:"Playfair Display",serif;font-weight:900;font-size:27px;letter-spacing:1px}
.foot-line{left:0;width:1200px;text-align:center;font-size:14px;color:#d4d4d4}
.copy{left:0;width:1200px;top:4594px;text-align:center;font-size:11px;color:var(--accent)}
.finale{left:350px;top:4650px;width:500px;height:429px;background:radial-gradient(ellipse 260px 110px at 50% 88%,#1e4a55 0%,#0f1e24 45%,transparent 75%)}
</style>
</head>
<body>

<header>
  <div class="abs brand">Harbor Wonder Hour</div>
  <nav class="abs nav"><span>EVENTS</span><span>PRICING</span><span>CONTACTS</span></nav>
  <div class="abs nav-btn">BUY TICKETS</div>
</header>

<section class="hero">
  <div class="abs hero-photo" role="img" aria-label="Three magicians in top hats and tuxedos performing card tricks amid smoke"></div>
  <div class="abs hero-frame"></div>
  <h1 class="abs hero-title big">PEOPLE</h1>
  <div class="abs hero-title small">ALWAYS LOVED MAGIC</div>
</section>

<section class="about">
  <div class="abs emblem" role="img" aria-label="Circular starburst emblem with crescent moon and star"></div>
  <div class="abs emblem-name">HARBOR WONDER HOUR</div>
  <div class="abs about-label">ABOUT ME</div>
  <p class="abs about-lead serif">Lorem ipsum dolor sit amet, consectetur adipiscing elit. Cras eu odio commodo, sodales tellus sit amet, tristique ante. Nunc ornare mauris ac odio suscipit, eget venenatis nisi viverra.</p>
  <p class="abs about-body">Donec hendrerit lectus urna, eu lacinia urna dignissim id. Fusce efficitur venenatis mi vel laoreet. Orci varius natoque penatibus et magnis dis parturient montes, nascetur ridiculus mus. Nam dictum risus tellus, ac dignissim libero finibus ut. Mauris ullamcorper ex et erat feugiat aliquet.</p>
  <div class="abs card-art" role="img" aria-label="Fan of tarot cards with zodiac wheel"></div>
</section>

<section class="monthly">
  <h2 class="outline-title" style="top:1580px">MONTHLY SHOW</h2>
  <div class="abs side-card" style="left:95px">
    <div class="side-date" style="left:0">NOV<b>13</b></div>
    <div class="side-text" style="left:14px">Lorem ipsum dolor sit amet</div>
    <div class="img" style="left:50px" role="img" aria-label="Magician performing"></div>
  </div>
  <div class="abs show-photo" role="img" aria-label="Magician in top hat and cape holding a wand"></div>
  <article class="abs show-card">
    <div class="kicker">Corporate Events</div>
    <div class="card-title">Lorem ipsum dolor sit amet, consectetur</div>
    <p class="card-copy">Donec hendrerit lectus urna, eu lacinia urna dignissim id. Fusce efficitur venenatis mi vel laoreet. Orci varius natoque pena tibus et magnis dis parturient montes.</p>
    <div class="meta" style="margin-top:20px"><svg width="14" height="14" viewBox="0 0 14 14"><circle cx="7" cy="7" r="6" fill="none" stroke="#ddd" stroke-width="1.3"/><path d="M7 3.5V7l2.5 1.5" fill="none" stroke="#ddd" stroke-width="1.3"/></svg>10:45 - 11:45 A.M</div>
    <div class="meta"><svg width="14" height="14" viewBox="0 0 14 14"><rect x="1" y="2" width="12" height="11" fill="none" stroke="#ddd" stroke-width="1.2"/><path d="M1 5h12M4 8h6M4 10.5h6" stroke="#ddd" stroke-width="1"/></svg>Monday- September 23</div>
    <div class="btn" style="margin-top:36px">BUY TICKET</div>
  </article>
  <div class="abs side-card" style="left:975px">
    <div class="img" style="left:0" role="img" aria-label="Performer in a witch hat"></div>
    <div class="side-date" style="left:82px">NOV<b>13</b></div>
    <div class="side-text" style="left:96px">Lorem ipsum dolor sit amet</div>
  </div>
  <div class="abs pager" style="top:2122px"><span>&larr;</span><span>3<small>/4</small></span><span>&rarr;</span></div>
</section>

<section class="media">
  <div class="abs side-word" style="left:95px;top:2150px;transform:rotate(180deg)">MAGIC</div>
  <div class="abs side-word" style="left:995px;top:2420px">SHOW</div>
  <div class="abs video" role="img" aria-label="Video still of a magician fanning playing cards"></div>
  <div class="abs video-title">Lorem ipsum dolor sit amet, consectetur adipiscing elit.</div>
  <svg class="abs" style="left:925px;top:2280px" width="50" height="22" viewBox="0 0 50 22"><circle cx="10" cy="11" r="9" fill="#fff"/><path d="M10 5v6l4 2" stroke="#000" stroke-width="1.8" fill="none"/><path d="M32 8v10h14V8M38 14c0-5 3-8 8-8M42 2l4 4-4 4" stroke="#fff" stroke-width="1.8" fill="none"/></svg>
  <svg class="abs play" width="90" height="90" viewBox="0 0 90 90" role="img" aria-label="Play video"><circle cx="45" cy="45" r="40" fill="rgba(0,0,0,.45)" stroke="#fff" stroke-width="2"/><path d="M37 30l22 15-22 15z" fill="#fff"/></svg>
  <div class="abs pager" style="top:2718px;gap:6px;font-size:22px;color:var(--accent)"><span>&larr;</span><span style="color:#ccc">/</span><span style="color:#ccc">&rarr;</span></div>
</section>

<section class="review">
  <div class="abs stars">
    <svg width="172" height="28" viewBox="0 0 172 28"><g fill="var(--accent)"><path id="s" d="M14 1l4 9 9.5 1-7 6.5 2 9.5-8.5-5-8.5 5 2-9.5-7-6.5 9.5-1z"/><use href="#s" x="36"/><use href="#s" x="72"/><use href="#s" x="108"/><use href="#s" x="144"/></g></svg>
  </div>
  <p class="abs quote">Nunc ornare mauris ac odio suscipit, eget venenatis nisi viverra. Donec hendrerit lectus urna, eu lacinia urna dignissim id. Fusce efficitur venenatis mi vel laoreet. Orci varius natoque penatibus et magnis dis parturient montes, nascetur ridiculus mus.</p>
  <div class="abs author">Sollicitudin Erat</div>
</section>

<section class="news">
  <h2 class="outline-title" style="top:3112px">LATEST NEWS</h2>
  <article class="abs news-card" style="left:125px;top:3250px">
    <div class="kicker">September 20, 2019</div>
    <div class="card-title">Lorem ipsum dolor sit amet, consectetur</div>
    <p class="card-copy">Lorem ipsum dolor sit amet, consectetur adipiscing elit. Cras eu odio commodo, sodales tellus sit amet, tristique ante. Nunc ornare mauris ac odio suscipit, eget venenatis nisi viverra. Donec hendrerit lectus urna, eu lacinia urna dignissim id. Fusce efficitur venenatis mi vel laoreet. Orci varius natoque penatibus et magnis dis parturient montes, nascetur ridiculus mus.</p>
    <div class="btn">READ MORE</div>
  </article>
  <article class="abs news-card" style="left:627px;top:3205px">
    <div class="kicker">September 20, 2019</div>
    <div class="card-title">Lorem ipsum dolor sit amet, consectetur</div>
    <p class="card-copy">Lorem ipsum dolor sit amet, consectetur adipiscing elit. Cras eu odio commodo, sodales tellus sit amet, tristique ante. Nunc ornare mauris ac odio suscipit, eget venenatis nisi viverra. Donec hendrerit lectus urna, eu lacinia urna dignissim id. Fusce efficitur venenatis mi vel laoreet. Orci varius natoque penatibus et magnis dis parturient montes, nascetur ridiculus mus.</p>
    <div class="btn">READ MORE</div>
  </article>
  <div class="abs pager" style="top:3710px"><span>&larr;</span><span>3<small>/4</small></span><span>&rarr;</span></div>
</section>

<section class="contact">
  <div class="abs wand-art" role="img" aria-label="Gloved hand holding a magic wand"></div>
  <h2 class="outline-title" style="top:3888px">STAY IN TOUCH</h2>
  <div class="abs field" style="left:228px;top:3968px;width:367px;height:47px">Your First Name</div>
  <div class="abs field" style="left:607px;top:3968px;width:368px;height:47px">Your Last Name</div>
  <div class="abs field" style="left:228px;top:4030px;width:367px;height:48px">Your Email Id.</div>
  <div class="abs field" style="left:607px;top:4030px;width:368px;height:48px">Phone No.</div>
  <div class="abs field" style="left:228px;top:4090px;width:747px;height:115px">Your Message</div>
  <div class="abs btn submit">SUBMIT NOW</div>
</section>

<footer>
  <div class="abs socials" role="img" aria-label="Social media links"><span></span><span></span><span></span><span></span></div>
  <div class="abs call">Call: 555 0142 318</div>
  <div class="abs foot-line" style="top:4516px">Kids Events &nbsp;&nbsp;•&nbsp;&nbsp; Corporate Events &nbsp;&nbsp;•&nbsp;&nbsp; Personal Events &nbsp;&nbsp;•&nbsp;&nbsp; Grand Show</div>
  <div class="abs foot-line" style="top:4541px">48 Lantern Pier Road, Bayview, WA 98001 &nbsp;•&nbsp; hello@harborwonderhour.example &nbsp;•&nbsp; Monday through Sunday, 24/7.</div>
  <div class="abs copy">© Copyright 2019 Harbor Wonder Hour. All Rights Reserved.</div>
  <div class="abs finale" role="img" aria-label="Falling playing cards above a top hat and wand in a spotlight"></div>
</footer>

</body>
</html>
```